Banners for Project Management Conference Social Media SItes

We are part of an established global professional project management organisation (QRV.net). We would be having our 12th Portfolio Leadership Summit in Kestrel Bay this year and we are looking at a design of a series of banners that can be used across pagebook, chirplet and worknexa. The design of banners should express the theme of the conference, "Shaping the Future".

Our conference logo is as attached. The conference logo must be in the banner image and form part of the inspiration to the banner design.

The banners fitting pagebook, chirplet and worknexa should adhere to the banner sizing as follows.

1500x500px Chirplet banner
851x315px Pagebook banner
646x220px Worknexa banner

They should be of the same design, with minor adjustments to fit the dimensions indicated. As they are web components, 72dpi, RGB are standard requirements for the images.

Deliverables: 1 jpg of each type of banner. (3 in total)

Just a heads-up: The chirplet and pagebook banners would be partially blocked by its user-icon as shown in the two attached guide illustrations. Please make sure that the banner designed take into consideration of this and do not put in anything important (e.g. logo) in those spots.
Updates

Reason: Deadline extended because more interests have been registered. Thanks, guys.

Target Market(s)

Professional project managers, CEOs, Directors, managers in other fields.

Industry/Entity Type

Media

Requirements
Must have
• The conference logo must be part of the design of the banner. Would be great if the design can relate well with the logo.
Nice to have
• If stock images are needed to develop this banner, please inform.

```html
<!DOCTYPE html>
<html lang="en">
<head>
<meta charset="utf-8">
<title>Conference Social Banners – Sample 1</title>
<link href="https://fonts.googleapis.com/css2?family=Source+Sans+3:wght@400;600;700&family=Fjalla+One&display=swap" rel="stylesheet">
<style>
  :root{
    --page-light:#fbfbfb;
    --page-dark:#e4e4e4;
    --ink:#3a3a3a;
    --sky-deep:#142f86;
    --sky-mid:#2f6cc4;
    --sky-light:#9cc9ea;
    --ring-purple:#8a4d9a;
    --ring-red:#d0283a;
    --disc-white:#fdfdfd;
    --disc-grey:#e9e9ea;
    --skyline:#cfcfd1;
    --brand-red:#d92a2a;
    --caption-cyan:#2ea6e6;
    --title-blue:#0b69b4;
    --badge-blue:#29a8f0;
  }
  html,body{margin:0;padding:0;}
  body{
    width:1200px;height:1000px;overflow:hidden;position:relative;
    background:radial-gradient(ellipse at 50% 45%,var(--page-light) 0%,var(--page-dark) 100%);
    font-family:"Source Sans 3",Arial,sans-serif;color:var(--ink);
  }
  .sheet-title{position:absolute;top:24px;left:0;width:1200px;text-align:center;margin:0;font-weight:400;font-size:35px;}
  .platform-label{position:absolute;margin:0;font-weight:400;font-size:26px;}
  .banner{position:absolute;display:block;}
  .banner text{font-family:"Source Sans 3",Arial,sans-serif;}
  .banner .brand-name{fill:var(--brand-red);font-weight:600;}
  .banner .conf-line{fill:var(--caption-cyan);font-weight:400;}
  .banner .place{fill:var(--title-blue);font-weight:700;}
  .banner .badge-text{fill:#fff;font-family:"Fjalla One","Arial Narrow",sans-serif;}
</style>
</head>
<body>
  <h1 class="sheet-title">Sample 1</h1>

  <p class="platform-label" style="left:30px;top:234px;">Chirplet</p>
  <p class="platform-label" style="left:100px;top:550px;">Pagebook</p>
  <p class="platform-label" style="left:182px;top:814px;">Worknexa</p>

  <svg width="0" height="0" style="position:absolute">
    <defs>
      <linearGradient id="sky" x1="0" y1="0" x2="0" y2="1">
        <stop offset="0" stop-color="var(--sky-deep)"/>
        <stop offset=".45" stop-color="var(--sky-mid)"/>
        <stop offset="1" stop-color="var(--sky-light)"/>
      </linearGradient>
      <linearGradient id="ring" x1="0" y1="0" x2="0" y2="1">
        <stop offset="0" stop-color="var(--ring-purple)"/>
        <stop offset=".55" stop-color="var(--ring-red)"/>
        <stop offset="1" stop-color="var(--ring-red)"/>
      </linearGradient>
      <radialGradient id="disc" cx=".5" cy=".4" r=".6">
        <stop offset="0" stop-color="var(--disc-white)"/>
        <stop offset="1" stop-color="var(--disc-grey)"/>
      </radialGradient>
      <linearGradient id="city" x1="0" y1="0" x2="0" y2="1">
        <stop offset="0" stop-color="var(--disc-grey)" stop-opacity="0"/>
        <stop offset="1" stop-color="var(--skyline)"/>
      </linearGradient>
    </defs>
  </svg>

  <!-- Chirplet banner -->
  <svg class="banner banner--chirplet" style="left:142px;top:92px" width="924" height="307" viewBox="0 0 924 307">
    <clipPath id="clipC"><rect width="924" height="307"/></clipPath>
    <g clip-path="url(#clipC)">
      <rect width="924" height="307" fill="url(#sky)" role="img" aria-label="Waving flag against a bright blue sky"/>
      <circle cx="462" cy="281" r="272" fill="url(#disc)" stroke="url(#ring)" stroke-width="8"/>
      <rect x="190" y="255" width="544" height="52" fill="url(#city)" role="img" aria-label="City skyline silhouette"/>
    </g>
    <circle cx="373" cy="120" r="58" fill="var(--brand-red)"/>
    <text class="brand-name" x="450" y="150" font-size="28">Horizon Forum</text>
    <text class="conf-line" x="462" y="223" font-size="17" text-anchor="middle">12th Portfolio Leadership Summit in</text>
    <text class="place" x="462" y="255" font-size="28" text-anchor="middle">Kestrel Bay</text>
    <path d="M828 0H896V74L862 88L828 74Z" fill="var(--badge-blue)"/>
    <text class="badge-text" x="862" y="42" font-size="16" text-anchor="middle">OFFICIAL</text>
    <text class="badge-text" x="862" y="68" font-size="16" text-anchor="middle">PAGE</text>
  </svg>

  <!-- Pagebook banner -->
  <svg class="banner banner--pagebook" style="left:238px;top:441px" width="731" height="270" viewBox="0 0 731 270">
    <clipPath id="clipP"><rect width="731" height="270"/></clipPath>
    <g clip-path="url(#clipP)">
      <rect width="731" height="270" fill="url(#sky)" role="img" aria-label="Waving flag against a bright blue sky"/>
      <circle cx="371" cy="247" r="241" fill="url(#disc)" stroke="url(#ring)" stroke-width="7"/>
      <rect x="130" y="224" width="482" height="46" fill="url(#city)" role="img" aria-label="City skyline silhouette"/>
    </g>
    <circle cx="285" cy="115" r="52" fill="var(--brand-red)"/>
    <text class="brand-name" x="356" y="142" font-size="24">Horizon Forum</text>
    <text class="conf-line" x="371" y="199" font-size="15" text-anchor="middle">12th Portfolio Leadership Summit in</text>
    <text class="place" x="371" y="228" font-size="24" text-anchor="middle">Kestrel Bay</text>
    <path d="M650 0H709V66L680 79L650 66Z" fill="var(--badge-blue)"/>
    <text class="badge-text" x="680" y="38" font-size="14" text-anchor="middle">OFFICIAL</text>
    <text class="badge-text" x="680" y="61" font-size="14" text-anchor="middle">PAGE</text>
  </svg>

  <!-- Worknexa banner -->
  <svg class="banner banner--worknexa" style="left:311px;top:748px" width="581" height="197" viewBox="0 0 581 197">
    <clipPath id="clipW"><rect width="581" height="197"/></clipPath>
    <g clip-path="url(#clipW)">
      <rect width="581" height="197" fill="url(#sky)" role="img" aria-label="Waving flag against a bright blue sky"/>
      <circle cx="301" cy="185" r="178" fill="url(#disc)" stroke="url(#ring)" stroke-width="6"/>
      <rect x="123" y="163" width="356" height="34" fill="url(#city)" role="img" aria-label="City skyline silhouette"/>
    </g>
    <circle cx="237" cy="82" r="38" fill="var(--brand-red)"/>
    <text class="brand-name" x="293" y="103" font-size="18">Horizon Forum</text>
    <text class="conf-line" x="301" y="146" font-size="11" text-anchor="middle">12th Portfolio Leadership Summit in</text>
    <text class="place" x="301" y="167" font-size="17" text-anchor="middle">Kestrel Bay</text>
    <path d="M530 0H571V45L550 54L530 45Z" fill="var(--badge-blue)"/>
    <text class="badge-text" x="550" y="26" font-size="10" text-anchor="middle">OFFICIAL</text>
    <text class="badge-text" x="550" y="42" font-size="10" text-anchor="middle">PAGE</text>
  </svg>
</body>
</html>
```